BIX Promotional flyer for students

We're looking for an 8.5" x 11" flyer that will be distributed to schools. Please see language to include in attached files.

Target Market(s)

The parents and teachers of high school students

Industry/Entity Type

Mental health

Other font styles liked:
• Monserrat and Roboto Slab

Requirements
Must have
• See attached pdf for language to be included on the flyer. Please use the color palette from our website: www.bixzone.tv. Please include some imagery of students. Please ensure the
Nice to have
• Feel free to use any of the graphics provided. See our website for our brand look & feel: www.bixzone.tv

```html
<!DOCTYPE html>
<html lang="en">
<head>
<meta charset="utf-8">
<title>Fundraise with BIX – Flyer</title>
<link href="https://fonts.googleapis.com/css2?family=Montserrat:wght@500;600;700;800;900&display=swap" rel="stylesheet">
<style>
  :root {
    --navy: #1b5580;
    --slate: #3f6590;
    --sky: #6f93b6;
    --deep: #1d4f7c;
    --clay: #9a6461;
    --teal: #3f7d82;
    --orange: #f07a2c;
    --white: #ffffff;
    --stage: #e8e8ea;
  }
  html, body {
    margin: 0;
    width: 1200px;
    height: 860px;
    overflow: hidden;
    background: var(--stage);
    font-family: "Montserrat", Arial, sans-serif;
  }
  .flyer-frame {
    position: absolute;
    left: 283px;
    top: 23px;
    width: 634px;
    height: 814px;
    box-shadow: 0 8px 24px rgba(0,0,0,0.18);
    overflow: hidden;
  }
  .flyer {
    position: absolute;
    left: 0; top: 0;
    width: 776px;
    height: 996px;
    transform: scale(0.817);
    transform-origin: top left;
    background: var(--navy);
    color: var(--white);
  }
  .flyer-shapes { position: absolute; left: 0; top: 0; }
  .brand {
    position: absolute;
    left: 50px; top: 84px;
    display: flex; align-items: center; gap: 12px;
  }
  .brand-dot {
    width: 44px; height: 44px; border-radius: 50%;
    background: var(--orange);
  }
  .brand-name {
    font-weight: 800; font-size: 46px; color: var(--white);
    letter-spacing: 1px;
  }
  .headline {
    position: absolute;
    right: 47px; top: 56px;
    text-align: right;
    font-weight: 700;
    line-height: 1;
  }
  .headline-top { font-size: 50px; letter-spacing: 1.5px; }
  .headline-bottom { display: flex; align-items: flex-end; justify-content: flex-end; gap: 12px; margin-top: 6px; }
  .headline-with {
    font-size: 50px; font-weight: 700;
    position: relative; padding-bottom: 12px;
  }
  .headline-with::after {
    content: ""; position: absolute; left: 0; right: 0; bottom: 0;
    height: 8px; border-radius: 4px; background: var(--orange);
  }
  .headline-name { font-size: 74px; font-weight: 900; color: var(--orange); letter-spacing: 2px; }
  .pill {
    position: absolute;
    background: var(--orange);
    color: var(--white);
    border-radius: 14px;
    font-weight: 700;
    text-align: center;
  }
  .pill-proceeds {
    left: 163px; top: 254px; width: 450px; height: 28px;
    line-height: 28px; font-size: 18px;
  }
  .pill-web {
    left: 163px; top: 922px; width: 450px; height: 26px;
    line-height: 26px; font-size: 14px; letter-spacing: 0.5px;
  }
  .cause {
    position: absolute;
    left: 50px; top: 484px;
    font-weight: 900; font-size: 44px; line-height: 56px;
    letter-spacing: 0.5px;
    text-shadow: 0 2px 6px rgba(0,0,0,0.35);
  }
  .about {
    position: absolute;
    right: 47px; top: 688px; width: 520px;
    text-align: right;
    font-weight: 600; font-size: 15px; line-height: 23px;
  }
</style>
</head>
<body>
  <div class="flyer-frame">
    <div class="flyer">
      <svg class="flyer-shapes" width="776" height="996" viewBox="0 0 776 996">
        <!-- header -->
        <rect x="0" y="0" width="776" height="195" fill="var(--navy)"/>
        <polygon points="0,0 400,0 60,340 0,340" fill="var(--slate)"/>
        <!-- middle band -->
        <rect x="0" y="195" width="776" height="145" fill="var(--sky)"/>
        <polygon points="0,195 200,195 60,340 0,340" fill="var(--slate)" opacity="0.6"/>
        <path d="M250 195 H585 V260 C585 310 540 340 500 340 H330 C290 340 250 310 250 260 Z" fill="var(--clay)"/>
        <path d="M140 340 A110 95 0 0 1 360 340 Z" fill="var(--deep)"/>
        <path d="M560 340 A110 115 0 0 1 730 260 L730 340 Z" fill="var(--navy)" opacity="0.45"/>
        <line x1="0" y1="268" x2="776" y2="268" stroke="var(--orange)" stroke-width="4"/>
        <!-- student photo -->
        <rect x="0" y="340" width="776" height="317" fill="url(#photoTone)" role="img" aria-label="Photo of high school students walking past a school sign"/>
        <path d="M640 657 A100 110 0 0 1 776 522 L776 657 Z" fill="var(--teal)" opacity="0.85"/>
        <!-- info band -->
        <rect x="0" y="657" width="776" height="146" fill="var(--sky)"/>
        <path d="M40 657 H240 A100 90 0 0 1 40 657 Z" fill="var(--slate)" opacity="0.35"/>
        <path d="M195 803 V760 C195 700 240 657 300 657 H525 V803 Z" fill="var(--clay)"/>
        <!-- sports photo -->
        <rect x="0" y="803" width="776" height="193" fill="url(#courtTone)" role="img" aria-label="Photo of students playing basketball on an outdoor court"/>
        <line x1="0" y1="935" x2="776" y2="935" stroke="var(--orange)" stroke-width="4"/>
        <defs>
          <linearGradient id="photoTone" x1="0" y1="0" x2="1" y2="1">
            <stop offset="0" stop-color="#4a4440"/>
            <stop offset="0.5" stop-color="#6b6660"/>
            <stop offset="1" stop-color="#3a3a3c"/>
          </linearGradient>
          <linearGradient id="courtTone" x1="0" y1="0" x2="0" y2="1">
            <stop offset="0" stop-color="#587ba2"/>
            <stop offset="1" stop-color="#3c5f88"/>
          </linearGradient>
        </defs>
      </svg>

      <div class="brand">
        <span class="brand-dot"></span>
        <span class="brand-name">bix</span>
      </div>

      <div class="headline">
        <div class="headline-top">FUNDRAISE</div>
        <div class="headline-bottom">
          <span class="headline-with">with</span>
          <span class="headline-name">BIX</span>
        </div>
      </div>

      <div class="pill pill-proceeds">50% of all proceeds Go back to your school</div>

      <div class="cause">SUPPORT THE<br>MENTAL HEALTH<br>OF YOUR STUDENTS</div>

      <p class="about">BIX is a simple and effective way to improve mental health. Your students will learn valuable coping skills and techniques from expert clinicians who analyze real cases and share their insights and advice</p>

      <div class="pill pill-web">BIXZONE.TV</div>
    </div>
  </div>
</body>
</html>
```